Business Card Design Project

We are VT Meridian, a recruitment company based in London. We require a new business card design in order to present our business. We work in a number of areas recruiting professional in areas such as engineering and rail. Most of our work is based in the Middle East so our cards must have a universal, professional feel.

Visit our website: http://www.vt-meridian.example.co.uk/ for more info

Industry/Entity Type

Business

Requirements
Must have
• Must be double sided

Must feature the companies logo on both sides of the card

Should incorporate the primary colours of the logo

Must be professional and contemporary, to fit in with the logo

Info: Name: Colin Prewett certRP MREC
Senior Recruitment Consultant
Address: 7 Quarry Row Fulwell London N41QZ
T: +44 (0)203 555 0147
M: +44 (0)7700 900 318
E: cprewett@vt-meridian.example.co.uk
W www.vt-meridian.example.co.uk
Nice to have
• A modern style card

```html
<!DOCTYPE html>
<html lang="en">
<head>
<meta charset="utf-8">
<title>VT Meridian – Business Card</title>
<link href="https://fonts.googleapis.com/css2?family=Open+Sans:wght@300;400;600&display=swap" rel="stylesheet">
<style>
  :root {
    --teal: #2a9a80;
    --teal-dark: #22826c;
    --ink: #4a4a4a;
    --ink-soft: #6b6b6b;
    --rule-grey: #d4d4d4;
    --card-white: #ffffff;
    --card-black: #1b1918;
    --backdrop: #e9e9e7;
  }
  * { margin: 0; padding: 0; box-sizing: border-box; }
  html, body {
    width: 1200px;
    height: 873px;
    overflow: hidden;
    background: var(--backdrop);
    font-family: "Open Sans", Arial, sans-serif;
  }
  .canvas {
    position: relative;
    width: 1200px;
    height: 873px;
  }
  .card {
    position: absolute;
    top: 286px;
    width: 520px;
    height: 302px;
    border-radius: 4px;
    overflow: hidden;
    box-shadow: 0 6px 18px rgba(0,0,0,0.18);
  }
  .card--front { left: 50px; background: var(--card-white); }
  .card--back  { left: 630px; background: var(--card-black); }

  /* front */
  .swoosh {
    position: absolute;
    left: 0; bottom: 0;
    width: 520px; height: 140px;
  }
  .contact-list {
    position: absolute;
    left: 28px; top: 24px;
    list-style: none;
    font-size: 11.5px;
    font-weight: 400;
    color: var(--ink);
    line-height: 19px;
  }
  .contact-list li { display: flex; align-items: center; gap: 8px; }
  .contact-icon { width: 12px; height: 12px; flex: none; }
  .contact-icon circle { fill: var(--teal); }
  .contact-icon path { fill: none; stroke: #fff; stroke-width: 1.3; stroke-linecap: round; stroke-linejoin: round; }

  .logo {
    position: absolute;
    display: flex;
    align-items: center;
    gap: 10px;
    white-space: nowrap;
  }
  .logo__mark {
    width: 38px; height: 38px;
    border-radius: 50%;
    background: var(--teal);
    flex: none;
  }
  .logo__name {
    font-weight: 400;
    font-size: 40px;
    letter-spacing: -1px;
    line-height: 1;
  }
  .card--front .logo { left: 26px; top: 112px; }
  .card--front .logo__name { color: var(--ink); }

  .person {
    position: absolute;
    right: 30px; top: 168px;
    color: var(--ink);
    white-space: nowrap;
  }
  .person__name {
    font-size: 22px;
    font-weight: 300;
    letter-spacing: -0.3px;
  }
  .person__creds {
    font-size: 10px;
    font-weight: 400;
    margin-left: 4px;
  }
  .person__role {
    font-size: 12.5px;
    font-weight: 400;
    color: var(--ink-soft);
    margin-top: 1px;
  }

  /* back */
  .card--back .logo { left: 110px; top: 94px; }
  .card--back .logo__name { color: #ffffff; }
  .website {
    position: absolute;
    left: 112px; top: 176px;
    font-size: 12px;
    font-weight: 600;
    color: var(--teal);
    letter-spacing: 0.2px;
  }
</style>
</head>
<body>
<main class="canvas">

  <section class="card card--front" aria-label="Business card front">
    <ul class="contact-list">
      <li>
        <svg class="contact-icon" viewBox="0 0 12 12"><circle cx="6" cy="6" r="6"/><path d="M4 3.2 L5 4.6 L4.5 5.3 Q5.4 6.9 6.7 7.5 L7.4 7 L8.8 8 L8.2 8.9 Q5.3 8.6 3.2 4 Z"/></svg>
        +44 (0)203 555 0147
      </li>
      <li>
        <svg class="contact-icon" viewBox="0 0 12 12"><circle cx="6" cy="6" r="6"/><path d="M4.5 2.8 H7.5 V9.2 H4.5 Z M5.6 8.2 H6.4"/></svg>
        +44 (0)7700 900 318
      </li>
      <li>
        <svg class="contact-icon" viewBox="0 0 12 12"><circle cx="6" cy="6" r="6"/><path d="M3 4 H9 V8.2 H3 Z M3 4 L6 6.3 L9 4"/></svg>
        cprewett@vt-meridian.example.co.uk
      </li>
      <li>
        <svg class="contact-icon" viewBox="0 0 12 12"><circle cx="6" cy="6" r="6"/><path d="M6 9.3 Q3.6 6.6 3.6 5 A2.4 2.4 0 0 1 8.4 5 Q8.4 6.6 6 9.3 Z"/></svg>
        7 Quarry Row Fulwell London N41QZ
      </li>
    </ul>

    <div class="logo">
      <span class="logo__mark"></span>
      <span class="logo__name">VT Meridian</span>
    </div>

    <div class="person">
      <div><span class="person__name">Colin Prewett</span><span class="person__creds">certRP MREC</span></div>
      <div class="person__role">Senior Recruitment Consultant</div>
    </div>

    <svg class="swoosh" viewBox="0 0 520 140" preserveAspectRatio="none" aria-hidden="true">
      <path d="M0 40 Q170 70 300 112 Q400 132 520 136 L520 140 L0 140 Z" fill="var(--rule-grey)"/>
      <path d="M0 58 Q150 90 270 124 Q360 140 420 140 L0 140 Z" fill="var(--teal)"/>
    </svg>
  </section>

  <section class="card card--back" aria-label="Business card back">
    <div class="logo">
      <span class="logo__mark"></span>
      <span class="logo__name">VT Meridian</span>
    </div>
    <div class="website">www.vt-meridian.example.co.uk</div>
  </section>

</main>
</body>
</html>
```